Morvex Business Card (intended for Business Card sized magnet)

Hi guys,

I would like to get a design for my business card for the restaurant. The design must be single sided as I intend to produce business card sized magnets.

The File attached must me on and I'm open for new ides

Can you please ensure that the design meets Cardowell's magnetic business card size specifications:

http://www.cardowell.example.au/custom-magnets.aspx?txi=15695&xnid=TopNav_Magnetic+Business+Cards+(linked+item)_Magnets_Marketing+Products&xnav=TopNav

Full Bleed Size (starting document size):
90 x 52 mm
1062 x 615 pixels
* Finished artwork should use the full bleed dimensions for best results.

Document Trim Size (final size after being cut):
87 x 49 mm
1028 x 579 pixels
* Please be sure to keep all text within the safe margin.

Resolution:
300 DPI

The winning design/source files need to meet these specifications.

Thanks
Updates

Hi guys, can I see more options please Thanks

```html
<!DOCTYPE html>
<html lang="en">
<head>
<meta charset="utf-8">
<title>Morvex Business Card</title>
<link href="https://fonts.googleapis.com/css2?family=Marcellus&family=Libre+Baskerville:wght@700&family=Permanent+Marker&family=Courier+Prime&display=swap" rel="stylesheet">
<style>
  :root {
    --parchment-light: #c99a5c;
    --parchment-mid: #a87139;
    --parchment-dark: #5e3517;
    --band-maroon: #4a1414;
    --band-maroon-deep: #2e0b0b;
    --ornament-dark: #2a100a;
    --ornament-faint: rgba(70, 40, 20, 0.35);
    --title-tan: #d7b07a;
    --contact-white: #fbf6ee;
    --strip-paper: rgba(176, 140, 96, 0.82);
    --ink: #1a120c;
    --web-tan: #caa06c;
  }
  * { margin: 0; padding: 0; box-sizing: border-box; }
  html, body { width: 1200px; height: 692px; overflow: hidden; background: #ffffff; }

  .card {
    position: relative;
    width: 1200px;
    height: 692px;
    overflow: hidden;
    background: radial-gradient(ellipse at 30% 40%, var(--parchment-light) 0%, var(--parchment-mid) 45%, var(--parchment-dark) 100%);
  }

  .texture {
    position: absolute;
    inset: 0;
    background: radial-gradient(ellipse at 75% 70%, rgba(210,170,110,0.45) 0%, rgba(0,0,0,0) 55%);
  }

  .brand-band {
    position: absolute;
    left: 410px;
    top: 0;
    width: 384px;
    height: 692px;
    background: linear-gradient(180deg, var(--band-maroon) 0%, var(--band-maroon-deep) 100%);
  }

  .ornament-strip {
    position: absolute;
    left: 0;
    top: 192px;
    width: 410px;
    height: 100px;
    background: var(--ornament-faint);
  }
  .ornament-strip--right { left: 794px; width: 406px; }

  .ornament-band {
    position: absolute;
    left: 410px;
    top: 182px;
    width: 384px;
    height: 112px;
    background: linear-gradient(180deg, var(--ornament-dark), #3d1a10 50%, var(--ornament-dark));
  }

  .brand-name {
    position: absolute;
    left: 416px;
    top: 42px;
    font-family: "Marcellus", serif;
    font-weight: 400;
    font-size: 98px;
    line-height: 1;
    color: var(--title-tan);
    letter-spacing: 1px;
  }

  .contact {
    position: absolute;
    left: 828px;
    top: 72px;
    color: var(--contact-white);
  }
  .contact__phone {
    font-family: "Libre Baskerville", serif;
    font-weight: 700;
    font-size: 38px;
    line-height: 1.2;
  }
  .contact__email {
    margin-top: 20px;
    font-family: Arial, Helvetica, sans-serif;
    font-size: 26px;
  }

  .address-strip {
    position: absolute;
    left: 180px;
    top: 388px;
    width: 860px;
    height: 150px;
    transform: rotate(12deg);
    transform-origin: center center;
    background: var(--strip-paper);
    box-shadow: 0 2px 6px rgba(0,0,0,0.25);
    display: flex;
    flex-direction: column;
    justify-content: center;
    padding-left: 70px;
  }
  .address {
    font-family: "Permanent Marker", cursive;
    font-style: normal;
    font-size: 32px;
    line-height: 1.3;
    color: var(--ink);
    white-space: nowrap;
  }
  .address__line { display: block; }
  .address__line--second { padding-left: 10px; }

  .website {
    position: absolute;
    left: 418px;
    top: 604px;
    font-family: "Courier Prime", monospace;
    font-size: 31px;
    color: var(--web-tan);
    letter-spacing: 1px;
  }
</style>
</head>
<body>
  <div class="card">
    <div class="texture"></div>
    <div class="ornament-strip" role="img" aria-label="Faint geometric star lattice border"></div>
    <div class="ornament-strip ornament-strip--right" role="img" aria-label="Faint geometric star lattice border"></div>
    <div class="brand-band"></div>
    <div class="ornament-band" role="img" aria-label="Geometric lattice ornament with three coloured jewels"></div>

    <h1 class="brand-name">Morvex</h1>

    <div class="contact">
      <div class="contact__phone">9480 3172</div>
      <div class="contact__email">morvex214@mailbox.example</div>
    </div>

    <div class="address-strip">
      <address class="address">
        <span class="address__line">214 Kelso Rd, Ashbury Park</span>
        <span class="address__line address__line--second">Melbourne, Victoria, Australia 3999</span>
      </address>
    </div>

    <div class="website">www.morvex.example.au</div>
  </div>
</body>
</html>
```